Web Design Project - (DESIGN AND FOLLOW UP CODING)

Web design for new management consultancy company

**About The Hadley Collective

We work with organisations find and implement creative and sensible solutions...

We explore and inform…We have in-house research capability and enrich discussion through our own research, analysis and inputs. We interview staff and stakeholders, analyse data and literature and help you develop knowledge and solutions, and the plans to implement these.

We present new ideas…We develop proposals and reports that use internally and externally derived evidence to propose effective new solutions.

Specialties
Higher Education, TAFE, Local Government, Regional Development

Industry
Education Management
Updates

LOGO added to brief (or email me on mavenlink@quorix.com.au to get copy

Target Market(s)

Business and government managers

Industry/Entity Type

Education

Requirements
Must have
• Sections:

**About
We work with organisations find and implement solutions to opportunities and challenges.
We explore and inform…
We present new ideas…

We develop proposals and reports that link internally and externally derived evidence to develop and implement new solutions.

Our three practice pillars are-
Ideas and partnerships:
Knowledgeable leaders:
Solutions:

** People
Marcus Pellow (PHOTO) Bio

** Services
Acumen - Solutions - Partnerships -Implementation
- On time and within budget.
- Project leadership.
- Researched inputs and facilitated outcomes.
- Focus on implementation.
- Develop value-adding partnerships and get them funded
- Creative responses to funding opportunities
- Organisational reviews

Sectors
-Education
-State Government
- Local Government
- Utilities
- Financial services
- Health and ageing
- Human services
- Government
-Regional

** Careers

** Key Partners
With weblinks

** Contact

Links to social link one LinkedIn social link two
Nice to have
• Logo available from: mavenlink@quorix.com.au

```html
<!DOCTYPE html>
<html lang="en">
<head>
<meta charset="utf-8">
<title>The Hadley Collective</title>
<link href="https://fonts.googleapis.com/css2?family=Montserrat:wght@400;500;600;700&display=swap" rel="stylesheet">
<style>
:root{
  --orange:#f15a22;
  --orange-light:#f6823b;
  --navy:#0f5a80;
  --ink:#555e66;
  --muted:#7c858c;
  --caption:rgba(28,44,58,.88);
  --white:#ffffff;
  --brand-ink:#26323c;
}
*{margin:0;padding:0;box-sizing:border-box}
html,body{width:775px;height:1200px;overflow:hidden;background:var(--white)}
body{position:relative;font-family:"Montserrat",Arial,sans-serif;color:var(--ink)}
.abs{position:absolute}

.hero{left:0;top:0;width:775px;height:432px;
  background:radial-gradient(ellipse at 45% 12%,#f4f8ee 0%,#bfe2e6 22%,#3c8fb4 48%,#0d3b5c 72%,#04111d 100%)}
.brand{left:84px;top:26px;display:flex;align-items:center;gap:8px}
.brand-mark{width:12px;height:12px;border-radius:50%;background:var(--orange)}
.brand-name{font-weight:500;font-size:15px;color:var(--brand-ink)}

.nav{left:84px;top:60px;width:607px;height:33px;background:var(--orange);display:flex;align-items:center;padding-left:18px}
.nav a{color:var(--white);text-decoration:none;font-size:9.5px;margin-right:21px;white-space:nowrap}
.search{position:absolute;right:14px;top:8px;width:120px;height:17px;background:var(--white);border-radius:2px;font-size:5.5px;color:#aaa;padding:5px 5px}
.search svg{position:absolute;right:4px;top:4px}

.caption{left:84px;top:200px;width:335px;height:118px;background:var(--caption);padding:17px 15px 0 15px}
.caption h1{font-weight:400;font-size:20px;color:var(--orange);margin-left:3px}
.caption p{color:var(--white);font-size:11.6px;line-height:18.5px;margin-top:7px}
.dots{left:368px;top:386px;display:flex;gap:1px}
.dots span{width:9px;height:9px;border-radius:50%;background:#555;border:1px solid #999}
.dots span.on{background:var(--white)}

.pillars{left:0;top:432px;width:775px;height:264px;background:var(--navy)}
.pillar{position:absolute;top:25px;width:194px}
.pillar h2{font-size:11.5px;font-weight:600;color:var(--white);margin-bottom:7px}
.pillar .tile{height:108px;background:radial-gradient(circle at 50% 45%,var(--orange-light),var(--orange) 70%);display:flex;align-items:center;justify-content:center}
.pillar p{font-size:7.6px;line-height:14.7px;color:#dce9f0;margin-top:12px;width:198px}

.col{position:absolute;top:716px}
.col h3{font-weight:400;font-size:12px;color:var(--ink);margin-bottom:12px;letter-spacing:.2px}
.photo{width:195px;height:112px;border:1px solid #ddd}
.col p.body{font-size:7.6px;line-height:14.3px;color:var(--muted);margin-top:11px;width:200px}
.ticks{list-style:none;margin-top:12px}
.ticks li{font-size:7.6px;color:var(--muted);height:19.5px;padding-left:20px;position:relative}
.ticks li::before{content:"";position:absolute;left:6px;top:2px;width:4px;height:4px;border-right:1.3px solid var(--orange);border-bottom:1.3px solid var(--orange);transform:rotate(-45deg)}

.news{position:absolute;left:498px;width:190px}
.news .thumb{position:absolute;left:0;top:0;width:64px;height:48px;border:2px solid #fff;box-shadow:0 0 2px #aaa}
.news .meta{position:absolute;left:75px;top:-2px;width:115px}
.news .date{font-size:9px;color:var(--ink)}
.news .title{font-size:7.8px;line-height:13px;color:var(--ink);margin-top:3px}
.news .by{font-size:7.4px;color:var(--muted);margin-top:3px}
.news .excerpt{position:absolute;left:0;top:64px;width:190px;font-size:7.6px;line-height:14.3px;color:var(--muted)}
.news .excerpt b{font-weight:400;color:var(--ink)}

.partner{position:absolute;width:130px;text-align:center;font-weight:600;font-size:14px;color:#555;display:flex;align-items:center;justify-content:center;gap:6px}
.partner i{display:inline-block;width:11px;height:11px;background:#666}

.footer{left:0;top:1140px;width:775px;height:60px;background:var(--navy)}
.footer nav{position:absolute;left:84px;top:20px;font-size:9px;color:var(--white)}
.footer nav a{color:var(--white);text-decoration:none}
.footer nav span{margin:0 9px}
.footer .copy{position:absolute;left:84px;top:37px;font-size:9px;color:#dce9f0}
.social{position:absolute;top:17px;width:26px;height:26px;border-radius:50%;background:var(--white)}
.footer .code{position:absolute;left:742px;top:28px;font-size:8px;color:#cfe0ea}
</style>
</head>
<body>

<div class="abs hero" role="img" aria-label="Concert crowd with raised arms silhouetted against bright stage lights"></div>

<div class="abs brand"><span class="brand-mark"></span><span class="brand-name">The Hadley Collective</span></div>

<nav class="abs nav">
  <a>Home</a><a>About</a><a>People</a><a>Services</a><a>Sectors</a><a>Careers</a><a>Key Partners</a><a>Contact</a>
  <div class="search">Type search
    <svg width="9" height="9" viewBox="0 0 9 9"><circle cx="3.6" cy="3.6" r="2.6" fill="none" stroke="#999" stroke-width="1"/><line x1="5.5" y1="5.5" x2="8" y2="8" stroke="#999" stroke-width="1.2"/></svg>
  </div>
</nav>

<div class="abs caption">
  <h1>The Hadley Collective</h1>
  <p>We interview staff and stakeholders, analyse data and literature and help you develop knowledge and solutions, and the plans to implement these.</p>
</div>
<div class="abs dots"><span class="on"></span><span></span><span></span><span></span></div>

<section class="abs pillars">
  <div class="pillar" style="left:84px">
    <h2>Ideas and partnerships</h2>
    <div class="tile">
      <svg width="30" height="62" viewBox="0 0 30 62" fill="#fff">
        <rect x="4" y="2" width="22" height="5" rx="2.5"/><rect x="3" y="9" width="24" height="5" rx="2.5"/><rect x="4" y="16" width="22" height="5" rx="2.5"/><rect x="5" y="23" width="20" height="5" rx="2.5"/>
        <path d="M2 31h26v10c0 6-5 10-13 10S2 47 2 41z"/><rect x="9" y="53" width="12" height="3"/><rect x="11" y="58" width="8" height="3" rx="1"/>
      </svg>
    </div>
    <p>Sed ut perspiciatis unde omnis iste natus error sit voluptatem accusantium doloremque laudantium, totam rem aperiam, ipsa quae ab illo inventore veritatis et quasi architecto beatae vitae dicta sunt explicabo.</p>
  </div>
  <div class="pillar" style="left:291px">
    <h2>Knowledgeable leaders</h2>
    <div class="tile">
      <svg width="84" height="50" viewBox="0 0 84 50" fill="#fff">
        <ellipse cx="20" cy="20" rx="10" ry="12" opacity=".85"/><ellipse cx="64" cy="20" rx="10" ry="12" opacity=".85"/>
        <path d="M0 48c0-10 8-16 20-16s14 4 14 8v8z" opacity=".85"/><path d="M84 48c0-10-8-16-20-16s-14 4-14 8v8z" opacity=".85"/>
        <ellipse cx="42" cy="16" rx="12" ry="14"/><path d="M18 50c0-12 10-19 24-19s24 7 24 19z"/>
      </svg>
    </div>
    <p>Sed ut perspiciatis unde omnis iste natus error sit voluptatem accusantium doloremque laudantium, totam rem aperiam, ipsa quae ab illo inventore veritatis et quasi architecto beatae vitae dicta sunt explicabo.</p>
  </div>
  <div class="pillar" style="left:497px">
    <h2>Solutions</h2>
    <div class="tile">
      <svg width="40" height="62" viewBox="0 0 40 62">
        <circle cx="20" cy="3" r="2.5" fill="#fff"/><circle cx="14" cy="9" r="2" fill="#fff"/><circle cx="24" cy="11" r="2" fill="#fff"/>
        <path d="M14 16h12v14l12 24c2 4 0 6-4 6H6c-4 0-6-2-4-6l12-24z" fill="none" stroke="#fff" stroke-width="3"/>
        <path d="M9 44h22l6 11c1 2 0 3-2 3H5c-2 0-3-1-2-3z" fill="#fff"/>
      </svg>
    </div>
    <p>Sed ut perspiciatis unde omnis iste natus error sit voluptatem accusantium doloremque laudantium, totam rem aperiam, ipsa quae ab illo inventore veritatis et quasi architecto beatae vitae dicta sunt explicabo.</p>
  </div>
</section>

<div class="col" style="left:84px">
  <h3>Our Company</h3>
  <div class="photo" role="img" aria-label="Business team in suits standing together on a white background" style="background:linear-gradient(180deg,#f4f4f4,#c9c9c9 60%,#8a8a8a)"></div>
  <p class="body">Ac cusamus e t iusto odio dignissimos ducimus qui blanditiis praesentium voluptatum deleniti atque corrupti quos dolores et quas molestias excepturi sint occaecati cupiditate non provident, similique sunt in culpa qui officia deserunt mollitia animi, id est laborum et dolorum fuga.<br>&nbsp;Et harum quidem rerum facilis est et expedita distinctio. Nam libero tempore, cum soluta nobis est eligendi optio cumque nihil impedit .</p>
</div>

<div class="col" style="left:290px">
  <h3>Why you choose us?</h3>
  <div class="photo" role="img" aria-label="Silhouetted business people beside a red question mark over a faint world map" style="background:linear-gradient(90deg,#eef1f4,#d4d8dc 45%,#3a3a3a 75%,#c0392b 95%)"></div>
  <p class="body">Ac cusamus e t iusto odio dignissimos ducimus qui blanditiis praesentium voluptatum deleniti atque corrupti quos dolores et quas molestias excepturi sint occaecati cupiditate non provident,</p>
  <ul class="ticks">
    <li>similique sunt in culpa</li>
    <li>qui officia deserunt mollitia</li>
    <li>animi, id est laborum</li>
  </ul>
</div>

<div class="col" style="left:498px"><h3>Latest News</h3></div>

<article class="news" style="top:746px">
  <div class="thumb" role="img" aria-label="Blue jigsaw puzzle pieces being fitted together" style="background:linear-gradient(135deg,#e8eef4,#2f7fd0 55%,#1c5ea8)"></div>
  <div class="meta"><div class="date">Aug 20 ,2013</div><div class="title">Sed ut perspiciatis unde omnis iste natus</div><div class="by">Posted By : Admin</div></div>
  <p class="excerpt">Accusantium doloremque laudantium, totam rem aperiam, eaque ipsa quae ab illo inven-tore veritatis et quasi &nbsp;<b>... Read More</b></p>
</article>

<article class="news" style="top:880px">
  <div class="thumb" role="img" aria-label="Colleagues talking in a bright office" style="background:linear-gradient(135deg,#f2ece6,#c9a88e 50%,#6d7d8c)"></div>
  <div class="meta"><div class="date">Aug 20 ,2013</div><div class="title">Sed ut perspiciatis unde omnis iste natus</div><div class="by">Posted By : Admin</div></div>
  <p class="excerpt">Accusantium doloremque laudantium, totam rem aperiam, eaque ipsa quae ab illo inven-tore veritatis &nbsp;<b>... Read More</b></p>
</article>

<div class="partner" style="left:111px;top:1025px">Larkfield Homes</div>
<div class="partner" style="left:245px;top:1030px">Brightcode</div>
<div class="partner" style="left:389px;top:1030px">Quillmark</div>
<div class="partner" style="left:530px;top:1025px"><i></i>Everline</div>
<div class="partner" style="left:111px;top:1088px">Tern Travels</div>
<div class="partner" style="left:245px;top:1088px">Nodeway</div>
<div class="partner" style="left:389px;top:1092px">Corvane Tech</div>
<div class="partner" style="left:530px;top:1088px">Lumen Concepts</div>

<footer class="abs footer">
  <nav><a>Home</a><span>|</span><a>About</a><span>|</span><a>People</a><span>|</span><a>Services</a><span>|</span><a>Sectors</a><span>|</span><a>Careers</a><span>|</span><a>Key Partners</a><span>|</span><a>Contact</a></nav>
  <div class="copy">© Company Name. 2013 All Rights Reserved</div>
  <a class="social" style="left:603px" aria-label="Social link one"></a>
  <a class="social" style="left:634px" aria-label="Social link two"></a>
  <a class="social" style="left:665px" aria-label="News feed"></a>
  <div class="code">C5</div>
</footer>

</body>
</html>
```